Agriculture new feeding concept for bull fattening needs a one-page flyer *

We are the innovation leader in the field of cattle feeding in Switzerland. Now we are launching a new “Tarsela” project for cattle fatteners, Munimäster (bull fattening). Tarsela is a complete fattening regime (feed, feed additives, services and advice).
Our sales representatives are with customers every day. You advertise the new project with the aim that our internal specialists get an appointment with the customer for a non-binding presentation of the project. This flyer is intended for this purpose.
Effect:
1. Innovative, modern
2. New
3. emotions
4. technical, scientific

You are also welcome to create a “logo” for Tarsela or choose / design your own lettering.
If you wish to use them, you will also find pictures of such fattening bulls in the appendix. However, pictures are not absolutely necessary.
Size A5, one-sided
Title: TARSELA - for beef fattening professionals
Text:
• Best fattening results
• Top customer service
• Innovative products
• Attractive conditions

Banner or similar:
May we introduce ourselves? or we would be happy to visit you. Etc.

```html
<!DOCTYPE html>
<html lang="de">
<head>
<meta charset="utf-8">
<title>Tarsela – Flyer für Rindfleischmastprofis</title>
<link href="https://fonts.googleapis.com/css2?family=Oswald:wght@300;400;500&family=Rokkitt:wght@400;500&family=Open+Sans:wght@600&display=swap" rel="stylesheet">
<style>
  :root {
    --page-bg: #e9e8e6;
    --paper: #ffffff;
    --navy-deep: #14306b;
    --navy: #1e4a96;
    --navy-light: #2b62b8;
    --pill: #1d3570;
    --tick: #6cc0f0;
    --text-light: #ffffff;
    --text-soft: #dfe7f5;
    --ink: #1d2a44;
  }
  * { margin: 0; padding: 0; box-sizing: border-box; }
  html, body { width: 1200px; height: 800px; overflow: hidden; background: var(--page-bg); }
  .flyer {
    position: absolute; left: 335px; top: 25px;
    width: 530px; height: 750px;
    background: var(--paper);
    box-shadow: 0 4px 18px rgba(0,0,0,.18);
    overflow: hidden;
  }
  .flyer-shapes { position: absolute; inset: 0; }
  .brand {
    position: absolute; top: 322px; left: 0; width: 504px;
    text-align: center; color: var(--text-light);
  }
  .brand-row { display: flex; align-items: center; justify-content: center; gap: 14px; }
  .brand-rule { width: 44px; height: 2px; background: var(--text-soft); opacity: .8; }
  .brand-name {
    font-family: "Oswald", sans-serif; font-weight: 500;
    font-size: 50px; letter-spacing: 7px; line-height: 1;
  }
  .brand-tagline {
    margin-top: 6px;
    font-family: "Oswald", sans-serif; font-weight: 300;
    font-size: 15px; letter-spacing: 1px; color: var(--text-soft);
  }
  .intro {
    position: absolute; left: 22px; top: 462px; width: 330px;
    font-family: "Oswald", sans-serif; font-weight: 300;
    font-size: 14.5px; line-height: 1.55; letter-spacing: .3px;
    color: var(--text-light); text-transform: uppercase;
  }
  .benefits { position: absolute; left: 22px; top: 532px; list-style: none; }
  .benefit {
    display: flex; align-items: center; gap: 11px; height: 29px;
    font-family: "Rokkitt", serif; font-weight: 400; font-size: 19px;
    color: var(--text-light);
  }
  .benefit svg { width: 15px; height: 15px; flex: none; }
  .invitation {
    position: absolute; top: 693px; left: 0; width: 100%; text-align: center;
    font-family: "Oswald", sans-serif; font-weight: 400; font-size: 11.5px;
    letter-spacing: .3px; color: var(--ink);
  }
  .contact-bar {
    position: absolute; left: 57px; top: 716px; width: 412px; height: 23px;
    background: var(--pill); border-radius: 12px;
    display: flex; align-items: center; justify-content: space-around;
    padding: 0 10px;
    font-family: "Open Sans", sans-serif; font-weight: 600; font-size: 10.5px;
    color: var(--text-light);
    box-shadow: 0 2px 4px rgba(0,0,0,.25);
  }
  .contact-item { display: flex; align-items: center; gap: 6px; }
  .contact-item svg { width: 12px; height: 12px; }
</style>
</head>
<body>
<main class="flyer">
  <svg class="flyer-shapes" viewBox="0 0 530 750" width="530" height="750">
    <defs>
      <linearGradient id="herdTones" x1="0" y1="0" x2="1" y2="1">
        <stop offset="0" stop-color="#a46b45"/>
        <stop offset=".45" stop-color="#d7c2a8"/>
        <stop offset=".75" stop-color="#8c5836"/>
        <stop offset="1" stop-color="#c9b79d"/>
      </linearGradient>
      <linearGradient id="bandTones" x1="0" y1="0" x2="0" y2="1">
        <stop offset="0" stop-color="var(--navy-deep)"/>
        <stop offset=".55" stop-color="var(--navy-light)"/>
        <stop offset="1" stop-color="var(--navy-deep)"/>
      </linearGradient>
      <radialGradient id="insetTonesA" cx=".5" cy=".5" r=".6">
        <stop offset="0" stop-color="#d9cdbb"/>
        <stop offset="1" stop-color="#8e6a4c"/>
      </radialGradient>
      <radialGradient id="insetTonesB" cx=".5" cy=".5" r=".6">
        <stop offset="0" stop-color="#c9c1b4"/>
        <stop offset="1" stop-color="#7d6a55"/>
      </radialGradient>
    </defs>
    <path class="hero-photo" role="img" aria-label="Photo of fattening bulls feeding at a barn feed rail"
          d="M0 75 Q55 12 160 0 L530 0 L530 410 L0 410 Z" fill="url(#herdTones)"/>
    <path class="blue-band" d="M0 362 Q245 262 530 378 L530 612 Q420 690 250 682 Q100 674 0 642 Z"
          fill="url(#bandTones)" stroke="var(--paper)" stroke-width="8"/>
    <circle class="inset-badge" cx="447" cy="521" r="72" fill="var(--navy-light)" stroke="var(--paper)" stroke-width="2"/>
    <circle class="inset-photo" role="img" aria-label="Close-up photo of a bull" cx="377" cy="457" r="47"
            fill="url(#insetTonesA)" stroke="var(--paper)" stroke-width="3"/>
    <circle class="inset-photo" role="img" aria-label="Photo of young bulls in a stable pen" cx="447" cy="521" r="62"
            fill="url(#insetTonesB)" stroke="var(--paper)" stroke-width="3"/>
  </svg>

  <header class="brand">
    <div class="brand-row">
      <span class="brand-rule"></span>
      <h1 class="brand-name">TARSELA</h1>
      <span class="brand-rule"></span>
    </div>
    <p class="brand-tagline">FÜR RINDFLEISCHMASTPROFIS</p>
  </header>

  <p class="intro">Tarsela ist eine komplette Mast Regime (Futtermittel, Futtermittelzusatzstoffe, Dienstleistungen und Beratung).</p>

  <ul class="benefits">
    <li class="benefit"><svg viewBox="0 0 16 16"><circle cx="8" cy="8" r="6.8" fill="none" stroke="var(--tick)" stroke-width="1.4"/><path d="M4.8 8.2 7.2 10.4 11.2 5.8" fill="none" stroke="var(--tick)" stroke-width="1.6" stroke-linecap="round" stroke-linejoin="round"/></svg>Beste Mattergebnisse</li>
    <li class="benefit"><svg viewBox="0 0 16 16"><circle cx="8" cy="8" r="6.8" fill="none" stroke="var(--tick)" stroke-width="1.4"/><path d="M4.8 8.2 7.2 10.4 11.2 5.8" fill="none" stroke="var(--tick)" stroke-width="1.6" stroke-linecap="round" stroke-linejoin="round"/></svg>Top Kundenservice</li>
    <li class="benefit"><svg viewBox="0 0 16 16"><circle cx="8" cy="8" r="6.8" fill="none" stroke="var(--tick)" stroke-width="1.4"/><path d="M4.8 8.2 7.2 10.4 11.2 5.8" fill="none" stroke="var(--tick)" stroke-width="1.6" stroke-linecap="round" stroke-linejoin="round"/></svg>Innovative Produkte</li>
    <li class="benefit"><svg viewBox="0 0 16 16"><circle cx="8" cy="8" r="6.8" fill="none" stroke="var(--tick)" stroke-width="1.4"/><path d="M4.8 8.2 7.2 10.4 11.2 5.8" fill="none" stroke="var(--tick)" stroke-width="1.6" stroke-linecap="round" stroke-linejoin="round"/></svg>Attraktive Bedingungen</li>
  </ul>

  <p class="invitation">DÜRFEN WIR UNS VORSTELLEN? ODER WIR WÜRDEN UNS FREUEN, SIE ZU BESUCHEN ...</p>

  <footer class="contact-bar">
    <span class="contact-item"><svg viewBox="0 0 12 12"><circle cx="6" cy="6" r="5.5" fill="#fff"/><rect x="3" y="4" width="6" height="4.2" rx=".5" fill="var(--pill)"/><path d="M3.2 4.3 6 6.4 8.8 4.3" fill="none" stroke="#fff" stroke-width=".7"/></svg>info@tarsela-mast.ch</span>
    <span class="contact-item"><svg viewBox="0 0 12 12"><circle cx="6" cy="6" r="5" fill="none" stroke="#fff" stroke-width="1"/><path d="M4.3 3.5c-.6.4-.7 1.2 0 2.4.8 1.4 1.8 2.3 2.7 2.5.6.1 1-.3 1.1-.7L7.2 7l-.7.4c-.5-.3-1.1-1-1.3-1.6l.6-.5-.5-1.1z" fill="#fff"/></svg>031 555 0148</span>
    <span class="contact-item"><svg viewBox="0 0 12 12"><circle cx="6" cy="6" r="5" fill="none" stroke="#fff" stroke-width="1"/><ellipse cx="6" cy="6" rx="2" ry="3.6" fill="none" stroke="#fff" stroke-width=".8"/><path d="M2.4 6h7.2" stroke="#fff" stroke-width=".8"/></svg>www.tarsela-mast.ch</span>
  </footer>
</main>
</body>
</html>
```